Harbor Fresh Cleaning car wrap

I need a car wrap design for my work van that is eye catching and stands out. My type of business is carpet cleaning and tile and grout cleaning along with other services. I would like the services to be listed on the wrap along with the phone number and website.
Also please add that we service Commercial and Residential.
Website is:
HarborFreshCleaning.com
Phone number (555) 203-4619
The services I provide are as follow:
Tile & Grout Cleaning
Carpet Cleaning
Hardwood Floor Cleaning and Refinishing
Upholstery and Rug Cleaning
My business colors consist of blue and white but I am open to using other colors.
My logo is attached in the files.
Commercial and Residential
Carpet Cleaning

```html
<!DOCTYPE html>
<html lang="en">
<head>
<meta charset="utf-8">
<title>Harbor Fresh Cleaning – Van Wrap</title>
<link rel="stylesheet" href="https://fonts.googleapis.com/css2?family=Roboto:wght@500;700;900&family=Roboto+Condensed:wght@500;700&display=swap">
<style>
  :root{
    --navy:#1b2a5c;
    --teal:#1f9a8c;
    --teal-light:#5cc2b3;
    --grey:#707070;
    --grey-dark:#3a3a3a;
    --glass:#9a9a9a;
    --white:#ffffff;
    --red:#d23a35;
    --tyre:#111111;
    --rim:#c9c9c9;
  }
  html,body{margin:0;padding:0;overflow:hidden;background:var(--white);}
  .wrap-sheet{display:block;width:1200px;height:1200px;}
  .body-outline{fill:none;stroke:var(--grey-dark);stroke-width:1.5;}
  .panel-navy{fill:var(--navy);}
  .panel-white{fill:var(--white);}
  .stripe-teal{fill:var(--teal);}
  .rocker{fill:var(--grey);}
  .glass{fill:var(--glass);stroke:var(--grey-dark);stroke-width:1.5;}
  .tyre{fill:var(--tyre);}
  .rim{fill:var(--rim);stroke:var(--grey);stroke-width:3;}
  .tail-light{fill:var(--red);}
  .logo-panel{fill:var(--white);}
  .brand-name{font-family:"Roboto",sans-serif;font-weight:900;fill:var(--navy);text-anchor:middle;}
  .phone{font-family:"Roboto",sans-serif;font-weight:700;}
  .phone-navy{fill:var(--navy);}
  .phone-white{fill:var(--white);}
  .web{font-family:"Roboto",sans-serif;font-weight:700;fill:var(--white);}
  .tagline{font-family:"Roboto",sans-serif;font-weight:500;fill:var(--white);text-anchor:middle;}
  .service{font-family:"Roboto Condensed",sans-serif;font-weight:700;text-anchor:middle;}
  .service-navy{fill:var(--navy);}
  .service-white{fill:var(--white);}
  .service-box{stroke:var(--teal-light);stroke-width:1.5;}
</style>
</head>
<body>
<svg class="wrap-sheet" viewBox="0 0 1024 1024" xmlns="http://www.w3.org/2000/svg" role="img" aria-label="Harbor Fresh Cleaning van wrap: driver side, passenger side and rear views">
  <defs>
    <linearGradient id="serviceFill" x1="0" y1="0" x2="1" y2="1">
      <stop offset="0" stop-color="#3fae9f"/>
      <stop offset="1" stop-color="#1b7f74"/>
    </linearGradient>
    <clipPath id="sideBody">
      <path d="M46 110 Q48 68 95 68 L622 68 Q660 70 700 100 L860 250 Q950 275 982 310 L990 420 L45 420 Z"/>
    </clipPath>
    <clipPath id="shortBody">
      <path d="M42 590 Q44 550 90 550 L645 550 L645 905 L40 905 Z"/>
    </clipPath>
    <clipPath id="rearBody">
      <path d="M700 590 Q700 552 740 552 L940 552 Q980 552 980 592 L985 880 L690 880 Z"/>
    </clipPath>
  </defs>

  <!-- Driver side view -->
  <g class="van van-side">
    <g clip-path="url(#sideBody)">
      <rect class="panel-white" x="0" y="60" width="1000" height="380"/>
      <polygon class="panel-navy" points="0,60 392,60 522,440 0,440"/>
      <polygon class="stripe-teal" points="372,60 384,60 512,440 500,440"/>
      <polygon class="stripe-teal" points="478,300 490,300 542,440 530,440"/>
      <rect class="rocker" x="0" y="362" width="1000" height="30"/>
      <rect class="rocker" x="900" y="330" width="100" height="110"/>
    </g>
    <path class="body-outline" d="M46 110 Q48 68 95 68 L622 68 Q660 70 700 100 L860 250 Q950 275 982 310 L990 420 L45 420 Z"/>
    <polygon class="glass" points="642,145 730,145 772,250 642,250"/>
    <polygon class="glass" points="738,145 752,145 828,250 782,250"/>
    <rect class="tail-light" x="44" y="268" width="26" height="62"/>
    <ellipse class="logo-panel" cx="430" cy="215" rx="170" ry="82"/>
    <text class="brand-name" x="430" y="208" font-size="34">HARBOR FRESH</text>
    <text class="brand-name" x="430" y="243" font-size="26">CLEANING</text>
    <text class="web" x="90" y="330" font-size="21">HarborFreshCleaning.com</text>
    <text class="phone phone-navy" x="537" y="347" font-size="33">(555) 203-4619</text>
    <circle class="tyre" cx="235" cy="428" r="60"/>
    <circle class="rim" cx="235" cy="428" r="34"/>
    <circle class="tyre" cx="840" cy="428" r="60"/>
    <circle class="rim" cx="840" cy="428" r="34"/>
  </g>

  <!-- Passenger side view -->
  <g class="van van-side-short">
    <g clip-path="url(#shortBody)">
      <rect class="panel-white" x="30" y="545" width="620" height="365"/>
      <polygon class="panel-navy" points="30,545 395,545 470,910 30,910"/>
      <polygon class="stripe-teal" points="375,545 387,545 462,910 450,910"/>
      <polygon class="stripe-teal" points="455,800 467,800 496,910 484,910"/>
      <rect class="rocker" x="30" y="835" width="620" height="28"/>
    </g>
    <path class="body-outline" d="M42 590 Q44 550 90 550 L645 550 L645 905 L40 905 Z"/>
    <rect class="tail-light" x="40" y="745" width="26" height="62"/>
    <text class="tagline" x="185" y="650" font-size="16">“Commercial &amp; Residential”</text>
    <polygon class="service-box" fill="url(#serviceFill)" points="72,664 298,664 288,708 298,752 72,752"/>
    <text class="service service-white" x="140" y="683" font-size="12.5">Tile &amp; Grout</text>
    <text class="service service-white" x="140" y="698" font-size="12.5">Cleaning</text>
    <text class="service service-white" x="238" y="683" font-size="12.5">Carpet</text>
    <text class="service service-white" x="238" y="698" font-size="12.5">Cleaning</text>
    <text class="service service-white" x="140" y="724" font-size="12.5">Hardwood Floor</text>
    <text class="service service-white" x="140" y="739" font-size="12.5">&amp; Refinishing</text>
    <text class="service service-white" x="238" y="724" font-size="12.5">Upholstery &amp;</text>
    <text class="service service-white" x="238" y="739" font-size="12.5">Rug Cleaning</text>
    <ellipse class="logo-panel" cx="460" cy="688" rx="150" ry="72"/>
    <text class="brand-name" x="460" y="682" font-size="30">HARBOR FRESH</text>
    <text class="brand-name" x="460" y="713" font-size="23">CLEANING</text>
    <text class="web" x="80" y="793" font-size="21">HarborFreshCleaning.com</text>
    <text class="phone phone-navy" x="636" y="817" font-size="20" text-anchor="end">(555) 203-4619</text>
    <circle class="tyre" cx="205" cy="905" r="60"/>
    <circle class="rim" cx="205" cy="905" r="34"/>
  </g>

  <!-- Rear view -->
  <g class="van van-rear">
    <g clip-path="url(#rearBody)">
      <rect class="panel-white" x="685" y="548" width="305" height="340"/>
      <polygon class="panel-navy" points="685,548 800,548 852,888 685,888"/>
      <polygon class="stripe-teal" points="822,730 834,730 858,888 846,888"/>
      <rect class="rocker" x="685" y="872" width="305" height="16"/>
    </g>
    <path class="body-outline" d="M700 590 Q700 552 740 552 L940 552 Q980 552 980 592 L985 880 L690 880 Z"/>
    <rect class="tail-light" x="810" y="548" width="55" height="7"/>
    <rect class="tail-light" x="690" y="748" width="18" height="58"/>
    <rect class="tail-light" x="967" y="748" width="18" height="58"/>
    <rect class="tyre" x="690" y="880" width="45" height="68" rx="6"/>
    <rect class="tyre" x="940" y="880" width="45" height="68" rx="6"/>
    <text class="phone" x="745" y="610" font-size="25"><tspan class="phone-white">(555)</tspan><tspan class="phone-navy"> 203-4619</tspan></text>
    <ellipse class="logo-panel" cx="845" cy="690" rx="112" ry="55"/>
    <text class="brand-name" x="845" y="686" font-size="22">HARBOR FRESH</text>
    <text class="brand-name" x="845" y="709" font-size="17">CLEANING</text>
    <text class="service service-white" x="775" y="774" font-size="12.5">Tile &amp; Grout</text>
    <text class="service service-white" x="775" y="789" font-size="12.5">Cleaning</text>
    <text class="service service-white" x="775" y="814" font-size="12.5">Carpet</text>
    <text class="service service-white" x="775" y="829" font-size="12.5">Cleaning</text>
    <text class="service service-navy" x="915" y="768" font-size="12">Hardwood Floor</text>
    <text class="service service-navy" x="915" y="782" font-size="12">Cleaning &amp;</text>
    <text class="service service-navy" x="915" y="796" font-size="12">Refinishing</text>
    <text class="service service-navy" x="915" y="816" font-size="12">Upholstery &amp;</text>
    <text class="service service-navy" x="915" y="830" font-size="12">Rug Cleaning</text>
  </g>
</svg>
</body>
</html>
```